Road Construction Company needs business cards

We would like a new business card designed for our business.

We're a road construction company based in Qld, Australia.

Can the business card please have the following information on it.

Name: Brent Malvoy
Position: General Manager
Phone: 0471 592 304
Email: Brent.malvoy@quendix.com.au
Address: 87 Harrowgate Ave, Pindarra, QLD, 4000
Website: www.quendix.com.au

Visually we'd like the card to be professional and simple.

Attached is our logo.

Our website is www.quendix.com.au

Target Market(s)

Men aged 25-60

Contact Information for Business Card

As listed in project description

Font styles to use
Serif

Requirements
Must have
• Large logo on back of card

```html
<!DOCTYPE html>
<html lang="en">
<head>
<meta charset="utf-8">
<title>Quendix Business Cards</title>
<link rel="stylesheet" href="https://fonts.googleapis.com/css2?family=Raleway:wght@400;500;700;800&display=swap">
<style>
  :root {
    --backdrop: #5d6670;
    --card-white: #ffffff;
    --card-black: #231f20;
    --brand-navy: #0b57a4;
    --brand-sky: #2a9bd8;
    --ink-white: #ffffff;
  }
  * { box-sizing: border-box; margin: 0; padding: 0; }
  html, body {
    width: 1200px; height: 900px; overflow: hidden;
    background: var(--backdrop);
    font-family: "Raleway", sans-serif;
  }
  .card-pair {
    position: absolute; left: 60px; top: 291px;
    display: flex; gap: 40px;
  }
  .card {
    width: 520px; height: 318px; position: relative; overflow: hidden;
    box-shadow: 0 14px 30px rgba(0,0,0,.35);
  }
  .card--front { background: var(--card-white); }
  .card--back { background: var(--card-black); display: flex; align-items: center; justify-content: center; }

  .wordmark {
    font-weight: 800; letter-spacing: 2px; text-transform: uppercase; line-height: 1;
  }
  .card--front .wordmark {
    position: absolute; left: 150px; top: 38px;
    font-size: 66px; color: var(--brand-navy);
  }
  .card--back .wordmark { font-size: 92px; color: var(--ink-white); }

  .holder { position: absolute; left: 36px; top: 128px; width: 200px; }
  .holder__name {
    font-size: 21px; font-weight: 700; color: var(--brand-navy);
    text-transform: uppercase; letter-spacing: -.3px;
  }
  .holder__role { font-size: 17px; font-weight: 400; color: var(--brand-sky); margin-top: 4px; }

  .divider {
    position: absolute; left: 246px; top: 124px; width: 1.5px; height: 80px;
    background: var(--brand-navy);
  }
  .contacts { position: absolute; left: 260px; top: 128px; list-style: none; }
  .contacts li {
    display: flex; align-items: center; gap: 8px;
    font-size: 13.5px; color: var(--brand-sky); height: 24px;
  }
  .icon { width: 17px; height: 17px; flex: none; }

  .address-band {
    position: absolute; left: 0; top: 232px; width: 100%; height: 40px;
    background: var(--brand-navy);
    display: flex; align-items: center; gap: 8px; padding-left: 36px;
    font-size: 15px; font-weight: 500; color: var(--ink-white);
  }
</style>
</head>
<body>
<div class="card-pair">
  <section class="card card--front">
    <div class="wordmark">Quendix</div>

    <div class="holder">
      <p class="holder__name">Brent Malvoy</p>
      <p class="holder__role">General Manager</p>
    </div>
    <div class="divider"></div>

    <ul class="contacts">
      <li>
        <svg class="icon" viewBox="0 0 20 20" aria-hidden="true">
          <circle cx="10" cy="10" r="10" fill="var(--brand-navy)"/>
          <path d="M7 5.5l1.6 2.4-1 1.1a6 6 0 0 0 3.4 3.4l1.1-1 2.4 1.6-.8 1.6c-3.6.2-7.9-4.1-7.7-7.7z" fill="#fff"/>
        </svg>
        0471 592 304
      </li>
      <li>
        <svg class="icon" viewBox="0 0 20 20" aria-hidden="true">
          <circle cx="10" cy="10" r="10" fill="var(--brand-navy)"/>
          <circle cx="10" cy="10" r="2.3" fill="none" stroke="#fff" stroke-width="1.4"/>
          <path d="M12.3 8v3.2c0 1.5 2.4 1.5 2.4-1.2a4.7 4.7 0 1 0-2 3.9" fill="none" stroke="#fff" stroke-width="1.4"/>
        </svg>
        Brent.malvoy@quendix.com.au
      </li>
      <li>
        <svg class="icon" viewBox="0 0 20 20" aria-hidden="true">
          <circle cx="10" cy="10" r="10" fill="var(--brand-navy)"/>
          <g fill="none" stroke="#fff" stroke-width="1.1">
            <circle cx="10" cy="10" r="5"/>
            <ellipse cx="10" cy="10" rx="2.2" ry="5"/>
            <path d="M5 10h10"/>
          </g>
        </svg>
        www.quendix.com.au
      </li>
    </ul>

    <div class="address-band">
      <svg class="icon" viewBox="0 0 20 20" aria-hidden="true">
        <circle cx="10" cy="10" r="10" fill="#fff"/>
        <path d="M10 4.5a3.6 3.6 0 0 0-3.6 3.6c0 2.6 3.6 7 3.6 7s3.6-4.4 3.6-7A3.6 3.6 0 0 0 10 4.5z" fill="var(--brand-navy)"/>
        <circle cx="10" cy="8.1" r="1.3" fill="#fff"/>
      </svg>
      87 Harrowgate Ave, Pindarra, QLD, 4000
    </div>
  </section>

  <section class="card card--back">
    <div class="wordmark">Quendix</div>
  </section>
</div>
</body>
</html>
```